Business Card Design Project

We have a logo, but would like to expand the use of it into a business card design. We are a B2B technology exchange platform for institutional investors to invest excess cash into short term assets matching their credit and pricing parameters. The assets are fractionalized and investors invest in portions.

Our customers are large, institutional, financial companies who are a bit traditional. We are high energy rebels with a cause...we are a disruptive technology and want to be viewed as a game changer but we need to present an image of trustworthiness and secure.

We are open not only to the image design but the material, die cut, etc. but want to stay in the traditional size of a business card.

We have other formats of the logo if needed. Our website is www.brambleharbor.com

I have posted a powerpoint template that we have been using.  This should not be considered the template we will use (after business cards we will have another project to incorporate business card design into powerpoint template) but just to give you a flavor of where we have been and have used in the past.

Target Market(s)

Institutional investors, asset managers, large fund institutions

Industry/Entity Type

Financial

Requirements
Must have
• Our logo
Traditional size
Nice to have
• unique use of logo, unique material, die cut, etc
Crisp, clean look
Use of both sides of card in a creative manner

```html
<!DOCTYPE html>
<html lang="en">
<head>
<meta charset="utf-8">
<title>Bramble Harbor – Business Card and Letter Pad</title>
<link href="https://fonts.googleapis.com/css2?family=Montserrat:wght@400;600;700&display=swap" rel="stylesheet">
<style>
  :root {
    --orange: #f39a2b;
    --orange-deep: #e8710a;
    --grey: #5f5f5f;
    --grey-light: #8a8a8a;
    --stock: #ebebe8;
    --paper: #ffffff;
    --backdrop: #d9d6d1;
    --line-white: #ffffff;
  }
  * { box-sizing: border-box; margin: 0; padding: 0; }
  html, body { width: 1200px; height: 900px; overflow: hidden; }
  body {
    background: var(--backdrop);
    font-family: "Montserrat", Arial, sans-serif;
    color: var(--grey);
    position: relative;
  }

  /* Letter pad */
  .letter-pad {
    position: absolute; left: 60px; top: 170px;
    width: 400px; height: 566px;
    background: var(--paper);
    box-shadow: 0 6px 18px rgba(0,0,0,.18);
    overflow: hidden;
  }
  .letter-pad .frame { position: absolute; inset: 0; }
  .letter-pad .brand { position: absolute; left: 52px; top: 118px; }
  .letter-pad .body-text {
    position: absolute; left: 52px; top: 190px; width: 300px;
    font-size: 8.5px; line-height: 1.6; color: #333;
  }
  .letter-pad .body-text p { margin-bottom: 9px; }

  /* Brand wordmark */
  .brand {
    display: flex; align-items: center; gap: 8px;
    font-weight: 700; color: var(--grey); white-space: nowrap;
  }
  .brand .dot { border-radius: 50%; background: var(--grey); flex: none; }
  .brand.small { font-size: 13px; }
  .brand.small .dot { width: 9px; height: 9px; }

  /* Cards */
  .card {
    position: absolute; width: 620px; height: 354px;
    box-shadow: 0 6px 18px rgba(0,0,0,.2);
    overflow: hidden;
  }

  .card-front { left: 520px; top: 90px; background: var(--orange); }
  .card-front .brand { position: absolute; left: 120px; top: 138px; font-size: 46px; }
  .card-front .brand .dot { width: 26px; height: 26px; }
  .card-front .rule {
    position: absolute; left: 0; right: 80px; height: 4px; background: var(--line-white);
  }
  .card-front .rule.one { top: 262px; }
  .card-front .rule.two { top: 274px; }
  .card-front .corner-mark {
    position: absolute; right: 22px; bottom: 22px;
    width: 76px; height: 76px; border-radius: 50%; background: var(--grey);
  }

  .card-back { left: 520px; top: 476px; background: var(--stock); }
  .card-back .holder { position: absolute; left: 34px; top: 30px; }
  .card-back .holder .name {
    font-size: 26px; font-weight: 700; color: var(--orange); letter-spacing: 1px;
  }
  .card-back .holder .role {
    font-size: 12px; font-weight: 600; letter-spacing: 3px; color: var(--grey); margin-top: 2px;
  }
  .card-back .phones { position: absolute; right: 32px; top: 30px; }
  .card-back .phones .row {
    display: flex; align-items: center; gap: 10px; justify-content: flex-end;
    font-size: 20px; font-weight: 600; color: var(--orange); margin-bottom: 4px;
  }
  .card-back .phones svg { width: 18px; height: 18px; }
  .card-back .brand { position: absolute; right: 32px; top: 112px; }
  .card-back .contacts { position: absolute; left: 150px; top: 108px; }
  .card-back .contacts .row {
    display: flex; align-items: center; gap: 12px;
    font-size: 17px; color: #4a4a4a; margin-bottom: 12px;
  }
  .card-back .contacts .icon { width: 24px; height: 24px; flex: none; }
  .card-back .contacts .square { background: var(--grey-light); border-radius: 3px; }
  .card-back .accent-line {
    position: absolute; left: 110px; right: 0; top: 240px; height: 4px; background: var(--orange);
  }
  .card-back .address { position: absolute; left: 180px; top: 254px; }
  .card-back .address .label { font-size: 12px; font-weight: 600; color: var(--orange); }
  .card-back .address .line { font-size: 17px; color: var(--grey); line-height: 1.35; }
  .card-back .corner-mark {
    position: absolute; left: 22px; bottom: 22px;
    width: 70px; height: 70px; border-radius: 50%; background: var(--orange);
  }
</style>
</head>
<body>

  <section class="letter-pad" aria-label="Letter pad">
    <svg class="frame" viewBox="0 0 400 566" width="400" height="566" aria-hidden="true">
      <path d="M60 40 H360 Q384 40 384 64 V566 H400 V0 H60 Z" fill="var(--orange-deep)"/>
      <path d="M40 90 Q40 66 64 66 H370 V80 H64 Q54 80 54 90 V566 H40 Z" fill="var(--orange-deep)"/>
    </svg>
    <div class="brand small"><span>Bramble Harbor</span><span class="dot"></span></div>
    <div class="body-text">
      <p>Dear Partner,</p>
      <p>Thank you for your continued interest in our exchange platform. We connect institutional investors with short term assets that match their credit and pricing goals.</p>
      <p>Our team is ready to walk you through each step, from onboarding to settlement, with clear reporting at every stage.</p>
      <p>We look forward to working with you.</p>
      <p>Sincerely,<br>Marcus Ellery</p>
    </div>
  </section>

  <section class="card card-front" aria-label="Business card front">
    <div class="brand"><span>Bramble Harbor</span><span class="dot"></span></div>
    <div class="rule one"></div>
    <div class="rule two"></div>
    <div class="corner-mark"></div>
  </section>

  <section class="card card-back" aria-label="Business card back">
    <div class="holder">
      <div class="name">Marcus Ellery</div>
      <div class="role">PRESIDENT &amp; CEO</div>
    </div>

    <div class="phones">
      <div class="row">
        <svg viewBox="0 0 18 18" aria-hidden="true"><rect x="5" y="1" width="8" height="16" rx="2" fill="var(--grey)"/><rect x="6.5" y="3" width="5" height="8" fill="var(--stock)"/></svg>
        <span>805.555.0142</span>
      </div>
      <div class="row">
        <svg viewBox="0 0 18 18" aria-hidden="true"><path d="M4 2 L7 2 L8 6 L6 7.5 Q8 11 10.5 12 L12 10 L16 11 L16 14 Q16 16 14 16 Q3 15 2 4 Q2 2 4 2 Z" fill="var(--grey)"/></svg>
        <span>818.555.0187</span>
      </div>
    </div>

    <div class="brand small"><span>Bramble Harbor</span><span class="dot"></span></div>

    <div class="contacts">
      <div class="row">
        <svg class="icon" viewBox="0 0 24 24" aria-hidden="true"><rect x="2" y="5" width="20" height="14" rx="1.5" fill="#fff" stroke="var(--grey-light)" stroke-width="1.5"/><path d="M2.5 6 L12 13 L21.5 6" fill="none" stroke="var(--grey-light)" stroke-width="1.5"/></svg>
        <span>mellery@brambleharbor.com</span>
      </div>
      <div class="row"><span class="icon square"></span><span>marcusellery</span></div>
      <div class="row"><span class="icon square"></span><span>www.brambleharbor.com</span></div>
    </div>

    <div class="accent-line"></div>
    <div class="address">
      <div class="label">Address</div>
      <div class="line">2210 Harborview Lane, Suite 118</div>
      <div class="line">Oakridge Falls, CA 90412</div>
    </div>
    <div class="corner-mark"></div>
  </section>

</body>
</html>
```